Granite, Brass and Shingle Roofing LLC needs a new business card

I need a new business card because I have a new address.
I do slate copper and tile roofs. My webpage is: www.granitebrassandshingleroofing.com

```html
<!DOCTYPE html>
<html lang="en">
<head>
<meta charset="utf-8">
<title>Granite, Brass &amp; Shingle Roofing – Business Card</title>
<link rel="stylesheet" href="https://fonts.googleapis.com/css2?family=Arimo:wght@400;700&family=Playfair+Display:wght@400&display=swap">
<style>
  :root {
    --page-bg: #e6e6e6;
    --card-white: #ffffff;
    --roof-blue: #529fcf;
    --name-blue: #4a9bd0;
    --ink: #0d0d0d;
  }
  * { box-sizing: border-box; margin: 0; padding: 0; }
  html, body {
    width: 1200px; height: 1200px; overflow: hidden;
    background: var(--page-bg);
  }
  .card {
    position: absolute; left: 262px;
    width: 686px; height: 392px;
    background: var(--card-white);
    overflow: hidden;
  }
  .card--front { top: 165px; }
  .card--back { top: 653px; }

  .front__band {
    position: absolute; left: 0; right: 0; top: 96px; bottom: 0;
    background: var(--roof-blue);
    border-top: 4px solid var(--ink);
  }
  .front__person {
    position: absolute; top: 30px; left: 0; width: 706px;
    text-align: center;
    font-family: "Arimo", Arial, sans-serif;
  }
  .person__name {
    font-weight: 700; font-size: 22px; color: var(--name-blue);
    letter-spacing: 0.2px;
  }
  .person__title { font-size: 15px; color: var(--ink); margin-top: 1px; }

  .brand-name {
    font-family: "Playfair Display", Georgia, serif;
    font-weight: 400; color: var(--ink);
    text-align: center; line-height: 1.12;
  }
  .front__brand {
    position: absolute; left: 70px; top: 218px; width: 250px;
    font-size: 24px;
  }
  .front__divider {
    position: absolute; left: 340px; top: 184px;
    width: 1px; height: 121px; background: var(--ink);
  }
  .front__contact {
    position: absolute; left: 360px; top: 190px;
    font-family: "Arimo", Arial, sans-serif; font-size: 14px;
    color: var(--ink); line-height: 19px;
    white-space: nowrap;
  }
  .contact__address { margin-bottom: 13px; }
  .contact__line { display: flex; align-items: center; gap: 8px; line-height: 20px; }
  .contact__line svg { width: 13px; height: 13px; flex: none; }

  .back__brand {
    position: absolute; left: 50%; top: 50%;
    transform: translate(-50%, -50%);
    display: flex; align-items: center; gap: 16px;
  }
  .back__mark { width: 22px; height: 22px; background: var(--roof-blue); flex: none; }
  .back__brand .brand-name { font-size: 32px; text-align: left; }
</style>
</head>
<body>
  <section class="card card--front" aria-label="Business card front">
    <div class="front__band"></div>
    <div class="front__person">
      <p class="person__name">Laszlo (Leo) Varga</p>
      <p class="person__title">Owner</p>
    </div>
    <p class="brand-name front__brand">Granite, Brass &amp; Shingle Roofing</p>
    <div class="front__divider"></div>
    <div class="front__contact">
      <p class="contact__address">2870 Millbrook Rd.<br>Millbrook, OH 44390</p>
      <p class="contact__line">
        <svg viewBox="0 0 24 24" aria-hidden="true"><path fill="#0d0d0d" d="M6.6 10.8a15.1 15.1 0 0 0 6.6 6.6l2.2-2.2c.3-.3.7-.4 1-.2 1.1.4 2.3.6 3.6.6.6 0 1 .4 1 1V20c0 .6-.4 1-1 1A17 17 0 0 1 3 4c0-.6.4-1 1-1h3.5c.6 0 1 .4 1 1 0 1.3.2 2.5.6 3.6.1.3 0 .7-.2 1z"/></svg>
        (440)555-0187
      </p>
      <p class="contact__line">
        <svg viewBox="0 0 24 24" aria-hidden="true"><path fill="#0d0d0d" d="M2 5h20v14H2z"/><path fill="none" stroke="#529fcf" stroke-width="1.8" d="M2.5 5.5 12 13l9.5-7.5"/></svg>
        gbsroofingllc@example.com
      </p>
      <p class="contact__line">
        <svg viewBox="0 0 24 24" aria-hidden="true"><circle cx="12" cy="12" r="10" fill="#0d0d0d"/><path fill="none" stroke="#529fcf" stroke-width="1.5" d="M2 12h20M12 2c3 3 3 17 0 20M12 2c-3 3-3 17 0 20"/></svg>
        www.granitebrassandshingleroofing.com
      </p>
    </div>
  </section>

  <section class="card card--back" aria-label="Business card back">
    <div class="back__brand">
      <span class="back__mark"></span>
      <p class="brand-name">Granite, Brass &amp;<br>Shingle Roofing</p>
    </div>
  </section>
</body>
</html>
```